Help me design my in store poster to promote our Loan product!

We need a design for a 2 X 3 poster inside our stores to promote our installment loan product. We are called Wade's Check Cashing, but offer loans inside our stores. We are open to a new logo for Wade's Loans, and open to any new exciting colors to stand out in the store. We provide short term monthly installment loans, we have monthly payments from 3 - 12 months. Our loans range from $100 - $1,400 with low interest. We ask for ID, consistent source of income, and credit check. We help build credit, and it is fast and easy. We want it to be simple and clean to get people's attention when they are inside our stores. Please help!

UPDATE: The design will be for a 2 X 7 poster now. Less words.

Other font styles liked:
• Rounded corners with the font

Requirements
Must have
• Bold colors, the words: loans, cash, $100 - $1,400, monthly payments, credit building, quick.
Nice to have
• A new logo, the Wade's Check Cashing logo added as reference

UPDATE: If we can add a quick slogan : FAST CASH NOW or HELP IS HERE or YOUR CASH IS HERE or LOANS FOR LIVING or LOANS FOR LIFE

A WADE'S FINANCE LOGO that looks similar to the NOVAJET logo I attached.

```html
<!DOCTYPE html>
<html lang="en">
<head>
<meta charset="utf-8">
<title>Wade's Check Cashing – Loans Poster</title>
<link rel="stylesheet" href="https://fonts.googleapis.com/css2?family=Montserrat:wght@900&display=swap">
<style>
  :root {
    --ink-blue: #0b5aa8;
    --paper: #ffffff;
    --cash-green: #3cc43c;
    --loan-green: #00984a;
    --alert-red: #ff0a0a;
    --sun-yellow: #ffcc00;
    --plum: #a84e8a;
    --art-tone: #d6e4f4;
  }
  html, body {
    margin: 0;
    padding: 0;
    overflow: hidden;
    background: var(--paper);
  }
  .poster {
    display: block;
    width: 800px;
    height: 1200px;
    background: var(--paper);
  }
  .poster text {
    font-family: "Montserrat", sans-serif;
    font-weight: 900;
    text-anchor: middle;
    dominant-baseline: central;
  }
  .art-area { fill: url(#art-glow); }
  .label-box {
    fill: var(--paper);
    stroke: var(--ink-blue);
    stroke-width: 5;
    stroke-linejoin: round;
  }
  .word {
    stroke: var(--paper);
    stroke-width: 6;
    paint-order: stroke;
    stroke-linejoin: round;
  }
  .word-cash { fill: var(--cash-green); font-size: 96px; }
  .word-range { fill: var(--alert-red); font-size: 40px; }
  .word-loans { fill: var(--loan-green); font-size: 80px; }
  .word-monthly { fill: var(--sun-yellow); font-size: 46px; }
  .word-quick { fill: var(--alert-red); font-size: 88px; }
  .word-credit { fill: var(--plum); font-size: 48px; }
  .brand-name { fill: var(--ink-blue); font-size: 22px; }
  .brand-dot { fill: var(--ink-blue); }
</style>
</head>
<body>
<svg class="poster" viewBox="0 0 800 1200" xmlns="http://www.w3.org/2000/svg" role="img" aria-label="Wade's Check Cashing loans poster">
  <defs>
    <radialGradient id="art-glow" cx="50%" cy="50%" r="50%">
      <stop offset="0%" stop-color="var(--art-tone)"/>
      <stop offset="70%" stop-color="var(--art-tone)" stop-opacity="0.6"/>
      <stop offset="100%" stop-color="var(--art-tone)" stop-opacity="0"/>
    </radialGradient>
  </defs>

  <!-- Brand -->
  <g class="brand">
    <circle class="brand-dot" cx="530" cy="92" r="9"/>
    <text class="brand-name" x="640" y="80">WADE'S</text>
    <text class="brand-name" x="640" y="106">CHECK CASHING</text>
  </g>

  <!-- Cash -->
  <g class="badge badge-cash">
    <ellipse class="art-area" role="img" aria-label="Comic cloud burst illustration with action lines" cx="240" cy="230" rx="220" ry="190"/>
    <g transform="translate(252,214) rotate(-7)">
      <rect class="label-box" x="-168" y="-60" width="336" height="120" rx="8"/>
      <text class="word word-cash" x="0" y="4">CASH</text>
    </g>
  </g>

  <!-- Amount range -->
  <g class="badge badge-range">
    <ellipse class="art-area" role="img" aria-label="Small comic cloud illustration with a star and action lines" cx="610" cy="360" rx="150" ry="130"/>
    <g transform="translate(612,370) rotate(17)">
      <rect class="label-box" x="-180" y="-30" width="360" height="60" rx="8"/>
      <text class="word word-range" x="0" y="2">$100 - $1,400</text>
    </g>
  </g>

  <!-- Loans -->
  <g class="badge badge-loans">
    <ellipse class="art-area" role="img" aria-label="Comic explosion burst illustration" cx="190" cy="620" rx="165" ry="160"/>
    <g transform="translate(204,632) rotate(-35)">
      <rect class="label-box" x="-170" y="-48" width="340" height="96" rx="8"/>
      <text class="word word-loans" x="0" y="3">LOANS</text>
    </g>
  </g>

  <!-- Monthly payments -->
  <g class="badge badge-monthly">
    <ellipse class="art-area" role="img" aria-label="Comic cloud burst illustration with action lines" cx="580" cy="675" rx="220" ry="190"/>
    <g transform="translate(576,672) rotate(8)">
      <rect class="label-box" x="-170" y="-64" width="340" height="128" rx="8"/>
      <text class="word word-monthly" x="0" y="-23">MONTHLY</text>
      <text class="word word-monthly" x="0" y="25">PAYMENTS</text>
    </g>
  </g>

  <!-- Quick -->
  <g class="badge badge-quick">
    <ellipse class="art-area" role="img" aria-label="Comic cloud illustration with a rocket launching upward" cx="230" cy="935" rx="225" ry="165"/>
    <g transform="translate(188,944) rotate(15)">
      <rect class="label-box" x="-175" y="-56" width="350" height="112" rx="8"/>
      <text class="word word-quick" x="0" y="4">QUICK</text>
    </g>
  </g>

  <!-- Credit building -->
  <g class="badge badge-credit">
    <ellipse class="art-area" role="img" aria-label="Comic cloud burst illustration with action lines" cx="600" cy="1020" rx="195" ry="170"/>
    <g transform="translate(596,1016) rotate(-20)">
      <rect class="label-box" x="-168" y="-64" width="336" height="128" rx="8"/>
      <text class="word word-credit" x="0" y="-24">CREDIT</text>
      <text class="word word-credit" x="0" y="25">BUILDING</text>
    </g>
  </g>
</svg>
</body>
</html>
```